Eye catching business card

2 sided
Black background with logo in color on one side along with the words "Proudly serving the commercial and defense industries since 1975"
2nd side to contain contact information (see attached current business card) and "Waterjet, Composite, Precision Machining and Clean Room Manufacturing" with a very faint watermark of a waving USA Flag in the back ground.
Remove the "est. 195" from the current logo design

```html
<!DOCTYPE html>
<html lang="en">
<head>
<meta charset="UTF-8">
<title>Keystone Forge – Business Card</title>
<link rel="stylesheet" href="https://fonts.googleapis.com/css2?family=Lato:wght@300;400;700&family=Questrial&display=swap">
<style>
  :root {
    --backdrop: #2c2c2e;
    --card-black: #050505;
    --card-band: #151515;
    --steel: #a9a9ab;
    --text-light: #c9c9cb;
    --text-soft: #9a9a9c;
    --accent-blue: #2a8fd8;
    --accent-deep: #1f63c7;
  }
  * { margin: 0; padding: 0; box-sizing: border-box; }
  html, body { width: 1200px; height: 800px; overflow: hidden; background: var(--backdrop); }
  .canvas { position: relative; width: 1200px; height: 800px; }

  .card {
    position: absolute; left: 390px; width: 420px; height: 240px;
    border-radius: 16px; overflow: hidden; background: var(--card-black);
  }
  .card--front { top: 130px; }
  .card--back { top: 430px; background: var(--card-band); }

  /* Front */
  .front-band { position: absolute; left: 0; top: 0; width: 420px; height: 240px; }
  .brand-mark {
    position: absolute; width: 40px; height: 40px; left: 190px; top: 52px;
    background: linear-gradient(135deg, var(--accent-blue), var(--accent-deep));
  }
  .brand-name {
    position: absolute; left: 0; width: 420px; top: 128px; text-align: center;
    font-family: 'Lato', sans-serif; font-weight: 700; font-size: 26px;
    color: var(--steel); letter-spacing: 1px;
  }
  .front-tagline {
    position: absolute; left: 0; width: 420px; top: 204px; text-align: center;
    font-family: 'Lato', sans-serif; font-weight: 300; font-size: 8.6px;
    line-height: 13.5px; letter-spacing: 2.6px; color: var(--text-soft);
  }

  /* Back */
  .flag-field { position: absolute; left: 0; top: 0; }
  .contact-name {
    position: absolute; right: 18px; top: 48px;
    font-family: 'Questrial', sans-serif; font-size: 20px; letter-spacing: 2.5px;
    color: var(--accent-blue);
  }
  .contact-role {
    position: absolute; right: 18px; top: 77px;
    font-family: 'Questrial', sans-serif; font-size: 10px; letter-spacing: 1.8px;
    color: var(--accent-blue);
  }
  .contact-rule {
    position: absolute; left: 195px; right: 18px; top: 93px; height: 1px;
    background: linear-gradient(90deg, rgba(31,99,199,0), var(--accent-deep) 30%, var(--accent-deep));
  }
  .contact-direct {
    position: absolute; right: 18px; top: 99px; text-align: right;
    font-family: 'Questrial', sans-serif; font-size: 10px; line-height: 10.5px;
    color: var(--steel);
  }
  .back-mark {
    position: absolute; left: 34px; top: 84px; width: 30px; height: 30px;
    background: linear-gradient(135deg, var(--accent-blue), var(--accent-deep));
  }
  .back-name {
    position: absolute; left: 0; width: 420px; top: 124px; text-align: center;
    font-family: 'Lato', sans-serif; font-weight: 700; font-size: 19px;
    color: var(--steel); letter-spacing: 1px;
  }
  .services {
    position: absolute; left: 0; width: 420px; top: 159px; text-align: center;
    font-family: 'Questrial', sans-serif; font-size: 10.4px; letter-spacing: 0.9px;
    color: var(--accent-blue);
  }
  .website {
    position: absolute; left: 0; width: 420px; top: 174px; text-align: center;
    font-family: 'Questrial', sans-serif; font-size: 10px; letter-spacing: 0.6px;
    color: var(--text-light);
  }
  .footer-col {
    position: absolute; top: 204px; width: 190px; text-align: center;
    font-family: 'Questrial', sans-serif; font-size: 7.4px; line-height: 13.5px;
    color: var(--text-light);
  }
  .footer-col--left { left: -8px; }
  .footer-col--right { left: 240px; }
</style>
</head>
<body>
<main class="canvas">

  <section class="card card--front" aria-label="Card front">
    <svg class="front-band" width="420" height="240" viewBox="0 0 420 240">
      <rect x="0" y="173" width="420" height="67" fill="var(--card-band)"/>
      <polygon points="178,173 242,173 210,199" fill="var(--card-black)"/>
    </svg>
    <div class="brand-mark"></div>
    <h1 class="brand-name">KEYSTONE FORGE</h1>
    <p class="front-tagline">PROUDLY SERVING THE COMMERCIAL AND<br>DEFENSE INDUSTRIES SINCE 1975</p>
  </section>

  <section class="card card--back" aria-label="Card back">
    <svg class="flag-field" width="420" height="240" viewBox="0 0 420 240" role="img" aria-label="Faint waving USA flag in the background">
      <defs>
        <linearGradient id="flagTone" x1="0" y1="0" x2="1" y2="0.4">
          <stop offset="0" stop-color="#1c2233"/>
          <stop offset="0.35" stop-color="#2a1a24"/>
          <stop offset="0.6" stop-color="#3a1522"/>
          <stop offset="0.8" stop-color="#2c2a30"/>
          <stop offset="1" stop-color="#3b1420"/>
        </linearGradient>
      </defs>
      <rect x="0" y="0" width="420" height="48" fill="#101010"/>
      <polygon points="0,48 172,48 210,22 248,48 420,48 420,193 248,193 210,218 172,193 0,193" fill="url(#flagTone)"/>
    </svg>

    <p class="contact-name">Dale Whitfield</p>
    <p class="contact-role">President</p>
    <div class="contact-rule"></div>
    <p class="contact-direct">Office: 555-210-0148<br>dale@keystoneforge.com</p>

    <div class="back-mark"></div>
    <h2 class="back-name">KEYSTONE FORGE</h2>
    <p class="services">Waterjet, Composite, Precision Machining and Clean Room Manufacturing</p>
    <p class="website">www.keystoneforge.com</p>

    <p class="footer-col footer-col--left">412 Mill Creek Rd. Brookvale, PA 17300<br>Phone: 555-210-0148</p>
    <p class="footer-col footer-col--right">Fax: 555-210-0150<br>info@keystoneforge.com</p>
  </section>

</main>
</body>
</html>
```